Meridian Payroll - Application form

I have an old application form in an editable PDF format (attached) which needs updating and bringing into the new branding. I would like both a word and editable PDF version of the application form

Target Market(s)

Contractors who are looking to join and use our umbrella services

Requirements
Must have
• All fields in the attached PDF version.
• Inline with the look and feel of the logo and web design attached.

```html
<!DOCTYPE html>
<html lang="en">
<head>
<meta charset="utf-8">
<title>Meridian Payroll – Application Form</title>
<link href="https://fonts.googleapis.com/css2?family=Carlito:wght@400;700&display=swap" rel="stylesheet">
<style>
  :root {
    --ink: #1a1a1a;
    --text: #2b2b2b;
    --field-fill: #e3e3e3;
    --field-border: #555555;
    --box-border: #8a8a8a;
    --band-1: #111111;
    --band-2: #555555;
    --band-3: #cfcfcf;
    --band-4: #eeeeee;
    --page: #ffffff;
  }
  * { margin: 0; padding: 0; box-sizing: border-box; }
  html, body { width: 849px; height: 1200px; overflow: hidden; background: var(--page); }
  body { font-family: "Carlito", "Calibri", Arial, sans-serif; color: var(--text); }
  .page { position: relative; width: 849px; height: 1200px; }

  .brand { position: absolute; left: 70px; top: 58px; display: flex; align-items: center; gap: 10px; }
  .brand-mark { width: 16px; height: 16px; background: var(--ink); }
  .brand-name { font-weight: 700; font-size: 24px; line-height: 26px; color: var(--ink); }

  .form-title { position: absolute; left: 0; width: 892px; top: 102px; text-align: center; font-size: 23.5px; font-weight: 700; color: var(--ink); }
  .title-rule { position: absolute; left: 419px; top: 130px; width: 66px; height: 4px; background: var(--ink); }

  .section-title { position: absolute; left: 0; width: 892px; text-align: center; font-size: 20.5px; font-weight: 700; text-decoration: underline; text-underline-offset: 3px; color: var(--ink); }
  .intro { position: absolute; font-size: 15.5px; line-height: 29px; }
  .intro-centered { left: 112px; width: 668px; text-align: center; }
  .intro-left { left: 102px; width: 690px; }

  .label, .option { position: absolute; font-size: 15.5px; line-height: 18px; white-space: nowrap; }
  .field { position: absolute; height: 24px; background: var(--field-fill); border: 1px dashed var(--field-border); }
  .option { padding-left: 18px; }
  .option::before { content: ""; position: absolute; left: 0; top: 3px; width: 11px; height: 11px; border: 1px solid var(--box-border); background: var(--page); }

  .band { position: absolute; left: 0; top: 1174px; width: 849px; height: 6px; display: flex; }
  .band span:nth-child(1) { width: 181px; background: var(--band-1); }
  .band span:nth-child(2) { width: 194px; background: var(--band-2); }
  .band span:nth-child(3) { width: 233px; background: var(--band-3); }
  .band span:nth-child(4) { flex: 1; background: var(--band-4); }
</style>
</head>
<body>
<div class="page">
  <div class="brand">
    <span class="brand-mark"></span>
    <span class="brand-name">Meridian<br>Payroll</span>
  </div>

  <h1 class="form-title">Application Form</h1>
  <div class="title-rule"></div>

  <h2 class="section-title" style="top:185px;">Your First Client</h2>
  <p class="intro intro-centered" style="top:217px;">Please add your initial client below - you’ll be able to add more later. If you’d prefer to provide details of your first client later, please miss this step out.</p>

  <span class="label" style="left:102px;top:338px;">Is this a recruitment agency or end client?</span>
  <span class="option" style="left:473px;top:341px;">Recruitment</span>
  <span class="option" style="left:583px;top:343px;">End Client:</span>

  <span class="label" style="left:102px;top:377px;">What is the name of your recruitment company or client?</span>
  <div class="field" style="left:478px;top:374px;width:310px;"></div>

  <span class="label" style="left:102px;top:406px;">Contact Name:</span>
  <div class="field" style="left:211px;top:403px;width:577px;"></div>

  <span class="label" style="left:102px;top:435px;">Address:</span>
  <div class="field" style="left:172px;top:432px;width:615px;"></div>

  <span class="label" style="left:102px;top:464px;">Town/City:</span>
  <div class="field" style="left:176px;top:461px;width:287px;"></div>
  <span class="label" style="left:472px;top:464px;">Country:</span>
  <div class="field" style="left:530px;top:461px;width:258px;"></div>

  <span class="label" style="left:102px;top:493px;">Postcode:</span>
  <div class="field" style="left:172px;top:490px;width:291px;"></div>

  <span class="label" style="left:102px;top:521px;">Telephone:</span>
  <div class="field" style="left:182px;top:518px;width:281px;"></div>
  <span class="label" style="left:472px;top:521px;">Email Address:</span>
  <div class="field" style="left:571px;top:518px;width:216px;"></div>

  <span class="label" style="left:102px;top:550px;">Proposed Start Date:</span>
  <div class="field" style="left:242px;top:547px;width:221px;"></div>
  <span class="label" style="left:472px;top:550px;">Proposed End Date:</span>
  <div class="field" style="left:603px;top:547px;width:185px;"></div>

  <span class="label" style="left:102px;top:579px;">Agency Rate:</span>
  <div class="field" style="left:197px;top:576px;width:268px;"></div>

  <span class="option" style="left:104px;top:610px;">Are you: Weekly</span>
  <span class="option" style="left:258px;top:612px;">Monthly Biller</span>

  <h2 class="section-title" style="top:674px;">Your Bank Details</h2>
  <p class="intro intro-left" style="top:706px;">We need your bank details in order to pay you. If you’d prefer to provide these details later, please miss this step out.</p>

  <span class="label" style="left:102px;top:797px;">Bank or Building Society Name:</span>
  <div class="field" style="left:310px;top:797px;width:477px;"></div>

  <span class="label" style="left:102px;top:826px;">Branch Name:</span>
  <div class="field" style="left:206px;top:826px;width:581px;"></div>

  <span class="label" style="left:102px;top:855px;">Branch Address:</span>
  <div class="field" style="left:218px;top:855px;width:569px;"></div>

  <span class="label" style="left:102px;top:884px;">Name of Account Holder(s):</span>
  <div class="field" style="left:287px;top:884px;width:500px;"></div>

  <span class="label" style="left:102px;top:913px;">Sort Code (6 Digits):</span>
  <div class="field" style="left:236px;top:913px;width:550px;"></div>

  <span class="label" style="left:102px;top:941px;">Building Society Number (if applicable):</span>
  <div class="field" style="left:358px;top:941px;width:428px;"></div>

  <span class="label" style="left:102px;top:970px;">Swift Code:</span>
  <div class="field" style="left:178px;top:970px;width:285px;"></div>
  <span class="label" style="left:472px;top:970px;">IBAN Number:</span>
  <div class="field" style="left:571px;top:970px;width:216px;"></div>

  <span class="label" style="left:102px;top:999px;">Account Number:</span>
  <div class="field" style="left:218px;top:999px;width:569px;"></div>

  <div class="band"><span></span><span></span><span></span><span></span></div>
</div>
</body>
</html>
```